Business card design needed

We are a wine business involved in winemaking, broking and packaging on behalf of clients globally with the majority being Asian. The design should be quite traditional and classic with some red used, font used should be easily read.

Target Market(s)

Trade customers other business owners

Industry/Entity Type

Business

Contact Information for Business Card

Rosalind Thwaite
Meridale Wine Collective
PO Box 738, Fenwick Vale
South Australia 5187
Phone: +61 (0)455 982 317
Email: kvcellars@brightmail.example

Logo styles of interest
Lettermark Logo

```html
<!DOCTYPE html>
<html lang="en">
<head>
<meta charset="utf-8">
<title>Meridale Wine Collective – Business Card</title>
<link rel="stylesheet" href="https://fonts.googleapis.com/css2?family=Archivo+Narrow:wght@400;700&family=Open+Sans:wght@400;600&display=swap">
<style>
  :root {
    --wine-red: #e31e24;
    --deep-red: #c1272d;
    --ink: #111111;
    --paper: #ffffff;
    --backdrop-top: #3a3a3a;
    --backdrop-bottom: #1c1c1c;
  }
  * { box-sizing: border-box; margin: 0; padding: 0; }
  html, body { width: 1200px; height: 1200px; overflow: hidden; }
  body {
    background: radial-gradient(circle at 50% 40%, var(--backdrop-top), var(--backdrop-bottom));
    position: relative;
    font-family: "Open Sans", sans-serif;
  }
  .card {
    position: absolute;
    left: 150px;
    width: 900px;
    height: 514px;
    box-shadow: 0 18px 40px rgba(0,0,0,.55);
    overflow: hidden;
  }
  .card--front { top: 70px; background: var(--wine-red); padding: 12px; }
  .card--back { top: 620px; background: var(--ink); }

  .front-face {
    position: relative;
    width: 100%;
    height: 100%;
    background: var(--paper);
    border-top: 5px solid var(--ink);
  }
  .front-title {
    position: absolute;
    left: 40px;
    top: 36px;
    font-family: "Archivo Narrow", sans-serif;
    font-size: 52px;
    font-weight: 400;
    color: var(--wine-red);
    white-space: nowrap;
  }
  .front-address {
    position: absolute;
    left: 110px;
    top: 130px;
    font-size: 30px;
    color: var(--ink);
    white-space: nowrap;
  }
  .contact-list {
    position: absolute;
    left: 300px;
    top: 200px;
    list-style: none;
    font-size: 27px;
    color: var(--ink);
  }
  .contact-list li { display: flex; align-items: center; gap: 16px; margin-bottom: 14px; white-space: nowrap; }
  .contact-icon { width: 40px; height: 30px; flex: none; }
  .front-footer { position: absolute; left: 0; bottom: 0; width: 876px; height: 150px; }

  .back-art { position: absolute; inset: 0; width: 100%; height: 100%; }
  .band-text {
    font-family: "Archivo Narrow", sans-serif;
    font-weight: 700;
    font-size: 36px;
    fill: var(--paper);
  }
  .footer-text {
    font-family: "Archivo Narrow", sans-serif;
    font-size: 17px;
    fill: var(--paper);
  }
</style>
</head>
<body>

<section class="card card--front" aria-label="Business card front">
  <div class="front-face">
    <h1 class="front-title">Rosalind Thwaite Meridale Wine Collective</h1>
    <p class="front-address">PO Box 738, Fenwick Vale South Australia 5187</p>
    <ul class="contact-list">
      <li>
        <svg class="contact-icon" viewBox="0 0 40 30" aria-hidden="true">
          <rect x="2" y="1" width="36" height="28" rx="6" fill="var(--wine-red)"/>
          <path d="M14 8c-2 2-2 6 2 10s8 5 10 3l-3-3-2 1c-2-1-4-3-5-5l1-2z" fill="var(--paper)"/>
        </svg>
        <span>+61 (0)455 982 317</span>
      </li>
      <li>
        <svg class="contact-icon" viewBox="0 0 40 30" aria-hidden="true">
          <rect x="2" y="3" width="36" height="24" fill="var(--wine-red)"/>
          <path d="M2 3l18 14L38 3" fill="none" stroke="var(--paper)" stroke-width="2.5"/>
        </svg>
        <span>kvcellars@brightmail.example</span>
      </li>
    </ul>
    <svg class="front-footer" viewBox="0 0 876 150" aria-hidden="true">
      <polygon points="0,126 520,72 520,80 0,136" fill="var(--ink)"/>
      <polygon points="0,140 520,86 520,96 0,150" fill="var(--wine-red)"/>
      <polygon points="470,62 520,24 876,24 876,150 470,150 520,96 520,62" fill="var(--wine-red)"/>
      <text class="footer-text" x="532" y="62" textLength="330" lengthAdjust="spacingAndGlyphs">Rosalind Thwaite Meridale Wine Collective</text>
    </svg>
  </div>
</section>

<section class="card card--back" aria-label="Business card back">
  <svg class="back-art" viewBox="0 0 900 514">
    <defs>
      <linearGradient id="glassTone" x1="0" y1="0" x2="1" y2="1">
        <stop offset="0" stop-color="#111111"/>
        <stop offset="0.55" stop-color="#2a0a0c"/>
        <stop offset="1" stop-color="#c1272d"/>
      </linearGradient>
    </defs>
    <rect x="0" y="0" width="460" height="514" fill="var(--wine-red)"/>
    <rect x="460" y="370" width="190" height="144" fill="var(--wine-red)"/>
    <rect x="560" y="20" width="340" height="270" fill="url(#glassTone)" role="img" aria-label="Wine glass illustration"/>
    <rect x="460" y="300" width="420" height="70" fill="var(--wine-red)"/>
    <rect x="880" y="300" width="20" height="70" fill="var(--paper)"/>
    <rect x="250" y="400" width="370" height="70" rx="35" fill="var(--ink)"/>
    <text class="band-text" x="278" y="448" textLength="300" lengthAdjust="spacingAndGlyphs">Rosalind Thwaite</text>
    <text class="band-text" x="478" y="348" textLength="385" lengthAdjust="spacingAndGlyphs">Meridale Wine Collective</text>
  </svg>
</section>

</body>
</html>
```